New Zealand Luggage Importer Needs Business Cards

We need professional, creative and fashionable business cards created.
We are based in New Zealand and import and distribute high-end, quality, fashionable and durable luggage.
We pride ourselves on selling the very best quality luggage, second only to 1 brand (which we won't mention here)...we use the same manufacturer. However, our prices are much more reasonable.
Industry/Entity Type
Business
Contact Information for Business Card
Mark Dunsley
027 512 4068
3/17 Harlow Street, Pinecrest Flats, Auckland, 0614
PO Box 204377, Fernside, Auckland 0731
09-528-3916
sales@brivancases.co.nz / www.brivancases.co.nz

```html
<!DOCTYPE html>
<html lang="en">
<head>
<meta charset="utf-8">
<title>Brivan Cases – Business Card</title>
<link rel="stylesheet" href="https://fonts.googleapis.com/css2?family=Tinos:wght@400;700&display=swap">
<style>
  :root {
    --page-bg: #e6e6e8;
    --card-white: #ffffff;
    --ink: #111111;
    --ink-soft: #2a2a2a;
    --icon: #3a3a3a;
    --teal: #3a9a8a;
    --charcoal: #2b2b2b;
    --photo-light: #d9d9d9;
    --photo-mid: #9a9a9a;
    --photo-dark: #5e5e5e;
    --logo-light: #ffffff;
  }
  * { box-sizing: border-box; margin: 0; padding: 0; }
  html, body {
    width: 1200px; height: 800px; overflow: hidden;
    background: var(--page-bg);
    font-family: "Tinos", "Times New Roman", serif;
  }
  .sheet {
    position: relative; width: 1200px; height: 800px;
    display: flex; align-items: center; justify-content: center; gap: 40px;
  }
  .card {
    position: relative; width: 540px; height: 308px; overflow: hidden;
    box-shadow: 0 6px 18px rgba(0,0,0,0.18);
  }

  /* Front side */
  .card--front { background: var(--card-white); }
  .card__photo {
    position: absolute; top: 0; right: 0; width: 62%; height: 100%;
    background:
      linear-gradient(90deg, var(--card-white) 0%, rgba(255,255,255,0) 45%),
      radial-gradient(ellipse at 70% 62%, var(--photo-mid) 0%, rgba(154,154,154,0) 38%),
      linear-gradient(180deg, var(--photo-light) 0%, var(--photo-mid) 70%, var(--photo-dark) 100%);
  }
  .card__logo {
    position: absolute; top: 22px; left: 28px;
    font-weight: 700; font-size: 22px; letter-spacing: 3px;
    color: var(--ink);
  }
  .card__name {
    position: absolute; top: 84px; left: 46px;
    font-weight: 700; font-size: 38px; color: var(--ink);
  }
  .contact {
    position: absolute; top: 176px; left: 34px;
    list-style: none; font-weight: 700; font-size: 13px; color: var(--ink-soft);
  }
  .contact__item {
    display: flex; align-items: flex-start; gap: 12px; margin-bottom: 6px; line-height: 1.25;
  }
  .contact__icon { width: 16px; height: 14px; flex: none; fill: var(--icon); margin-top: 1px; }

  /* Back side */
  .card--back {
    background: linear-gradient(210deg, var(--teal) 0%, #2f7a6e 35%, var(--charcoal) 75%);
    display: flex; align-items: center; justify-content: center;
  }
  .card__logo--back {
    position: static; color: var(--logo-light);
    font-size: 38px; letter-spacing: 6px;
  }
</style>
</head>
<body>
<main class="sheet">
  <section class="card card--front" aria-label="Business card front">
    <div class="card__photo" role="img" aria-label="Black and white photo of a suitcase standing on a patterned tiled pavement"></div>
    <div class="card__logo">BRIVAN CASES</div>
    <h1 class="card__name">Mark Dunsley</h1>
    <ul class="contact">
      <li class="contact__item">
        <svg class="contact__icon" viewBox="0 0 16 16" aria-hidden="true"><path d="M3 1h3l1.5 4-2 1.3a9 9 0 0 0 4.2 4.2L11 8.5l4 1.5v3a2 2 0 0 1-2 2A12 12 0 0 1 1 3a2 2 0 0 1 2-2z"/></svg>
        <span>027 512 4068</span>
      </li>
      <li class="contact__item">
        <svg class="contact__icon" viewBox="0 0 16 14" aria-hidden="true"><path d="M0 2h16v10H0z M1 3l7 5 7-5" stroke="#fff" stroke-width="1"/></svg>
        <span>sales@brivancases.co.nz</span>
      </li>
      <li class="contact__item">
        <svg class="contact__icon" viewBox="0 0 16 16" aria-hidden="true"><circle cx="8" cy="8" r="7" fill="none" stroke="#3a3a3a" stroke-width="1.4"/><path d="M1 8h14M8 1c-3 3-3 11 0 14M8 1c3 3 3 11 0 14" fill="none" stroke="#3a3a3a" stroke-width="1.2"/></svg>
        <span>www.brivancases.co.nz</span>
      </li>
      <li class="contact__item">
        <svg class="contact__icon" viewBox="0 0 16 14" aria-hidden="true"><path d="M8 1L1 7h2v6h4V9h2v4h4V7h2z" fill="none" stroke="#3a3a3a" stroke-width="1.4"/></svg>
        <span>3/17 Harlow Street, Pinecrest Flats, Auckland, 0614<br>PO Box 204377, Fernside, Auckland 0731</span>
      </li>
    </ul>
  </section>

  <section class="card card--back" aria-label="Business card back">
    <div class="card__logo card__logo--back">BRIVAN CASES</div>
  </section>
</main>
</body>
</html>
```